Lavoie Roofing

Want a professional looking business card

Industry/Entity Type

Business

Contact Information for Business Card

Mark Lavoie ( Owner) mark@lavoieroofing.example, www.lavoieroofing.example, Adress: 4712 County road 31 Cedarvale K0B2M4

```html
<!DOCTYPE html>
<html lang="en">
<head>
<meta charset="utf-8">
<title>Lavoie Roofing – Business Card</title>
<link rel="stylesheet" href="https://fonts.googleapis.com/css2?family=Exo+2:wght@400;600;800&display=swap">
<style>
  :root {
    --backdrop: #eeecee;
    --card-black: #0b0b0c;
    --card-white: #ffffff;
    --brand-blue: #1c4384;
    --text-white: #ffffff;
    --text-soft: #e6ebf5;
    --shadow: rgba(0, 0, 0, 0.22);
  }
  * { box-sizing: border-box; margin: 0; padding: 0; }
  html, body {
    width: 1200px;
    height: 1000px;
    overflow: hidden;
    background: var(--backdrop);
    font-family: "Exo 2", sans-serif;
  }
  .stage {
    width: 1200px;
    height: 1000px;
    display: flex;
    align-items: center;
    justify-content: center;
    gap: 40px;
  }
  .card {
    position: relative;
    width: 520px;
    height: 300px;
    border-radius: 22px;
    box-shadow: 0 14px 30px var(--shadow);
    overflow: hidden;
  }
  .card--front {
    background: var(--card-black);
    display: flex;
    align-items: center;
    justify-content: center;
  }
  .brand {
    display: flex;
    align-items: center;
    gap: 12px;
    font-weight: 800;
    text-transform: uppercase;
    letter-spacing: 0.06em;
    white-space: nowrap;
  }
  .brand__mark {
    width: 18px;
    height: 18px;
    background: currentColor;
    flex: none;
  }
  .card--front .brand {
    color: var(--text-white);
    font-size: 38px;
  }
  .card--back {
    background: var(--card-white);
  }
  .card--back .brand {
    position: absolute;
    left: 26px;
    top: 133px;
    color: var(--brand-blue);
    font-size: 17px;
    gap: 7px;
    letter-spacing: 0.04em;
  }
  .card--back .brand__mark { width: 10px; height: 10px; }
  .contact-bubble {
    position: absolute;
    inset: 0;
    width: 520px;
    height: 300px;
  }
  .contact-bubble path { fill: var(--brand-blue); }
  .contact {
    position: absolute;
    left: 266px;
    top: 68px;
    width: 220px;
    color: var(--text-soft);
    font-size: 13px;
    line-height: 1.35;
  }
  .contact__name {
    color: var(--text-white);
    font-weight: 600;
    font-size: 16px;
    margin-bottom: 12px;
  }
  .contact__lines { margin-bottom: 12px; }
</style>
</head>
<body>
  <main class="stage">
    <section class="card card--front" aria-label="Business card front">
      <div class="brand"><span class="brand__mark"></span><span>Lavoie Roofing</span></div>
    </section>

    <section class="card card--back" aria-label="Business card back">
      <div class="brand"><span class="brand__mark"></span><span>Lavoie Roofing</span></div>
      <svg class="contact-bubble" viewBox="0 0 520 300" aria-hidden="true">
        <path d="M250,46 H372 C448,46 492,98 492,150 C492,200 462,236 418,242 L436,284 L384,244 H250 Z"/>
      </svg>
      <div class="contact">
        <p class="contact__name">Mark Lavoie | Owner</p>
        <p class="contact__lines">mark@lavoieroofing.example<br>www.lavoieroofing.example</p>
        <p class="contact__address">4712 County road 31,<br>Cedarvale K0B2M4</p>
      </div>
    </section>
  </main>
</body>
</html>
```